Whitmore Business Card Design

The name of the business is Dara Whitmore, CPA LLC
The service that we offer is Accounting, Tax & Consulting Services. I need it to have the following items:
Dara Whitmore, Principal
Phone Number
Email Address
Physical Address

I have attached the company logo, one in black and one in white. Please provide a design in black background and the other in white background. Please include "Accounting, Tax & Consulting Services". I want the business card to be clean and very professional.

```html
<!DOCTYPE html>
<html lang="en">
<head>
<meta charset="utf-8">
<title>Dara Whitmore, CPA LLC – Business Cards</title>
<link href="https://fonts.googleapis.com/css2?family=Montserrat:wght@500;600;700&family=Roboto:wght@300;400&display=swap" rel="stylesheet">
<style>
  :root {
    --backdrop: #2a2a2a;
    --card-dark: #1f1f21;
    --card-dark-edge: #2c2c2e;
    --card-light: #f2f2f2;
    --card-light-edge: #dedede;
    --brand-red: #8e1b1b;
    --ink-dark: #3a3a3c;
    --ink-mid: #7b7b7d;
    --ink-soft: #9c9c9e;
    --ink-white: #f1f1f1;
    --rule: #8a8a8a;
  }
  * { margin: 0; padding: 0; box-sizing: border-box; }
  html, body {
    width: 1200px; height: 1138px; overflow: hidden;
    background: var(--backdrop);
  }
  .canvas { position: relative; width: 1200px; height: 1138px; }

  .card {
    position: absolute;
    width: 621px; height: 375px;
    border-radius: 16px;
    box-shadow: 0 6px 14px rgba(0,0,0,.45);
  }
  .card--front {
    left: 272px; top: 184px;
    background: linear-gradient(160deg, var(--card-dark) 0%, var(--card-dark-edge) 100%);
  }
  .card--back {
    left: 274px; top: 606px;
    background: linear-gradient(180deg, var(--card-light) 0%, var(--card-light-edge) 100%);
  }

  .firm-name {
    font-family: 'Montserrat', sans-serif;
    font-weight: 600;
    letter-spacing: 0.5px;
    white-space: nowrap;
  }
  .firm-tagline {
    font-family: 'Montserrat', sans-serif;
    font-weight: 600;
    letter-spacing: 2.4px;
    white-space: nowrap;
  }
  .firm-services {
    font-family: 'Montserrat', sans-serif;
    font-weight: 500;
    font-size: 13px;
    letter-spacing: 1.2px;
    white-space: nowrap;
  }

  /* Front */
  .front-lockup {
    position: absolute; left: 0; right: 0; top: 100px;
    display: flex; flex-direction: column; align-items: center;
  }
  .front-lockup .brand-square {
    width: 84px; height: 84px; background: var(--brand-red);
    margin-bottom: 20px;
  }
  .front-lockup .firm-name { font-size: 27px; color: var(--ink-white); }
  .front-lockup .firm-tagline { font-size: 17.5px; color: var(--ink-soft); margin-top: 4px; }
  .front-lockup .firm-services { color: var(--ink-soft); margin-top: 10px; }

  /* Back */
  .back-lockup {
    position: absolute; left: 30px; top: 42px;
    display: flex; align-items: flex-start; gap: 16px;
  }
  .back-lockup .brand-square {
    width: 72px; height: 72px; background: var(--brand-red);
  }
  .back-lockup .firm-name { font-size: 26px; color: var(--ink-dark); margin-top: 4px; }
  .back-lockup .firm-tagline { font-size: 17.5px; color: var(--ink-mid); margin-top: 2px; }
  .back-lockup .firm-services { color: var(--ink-mid); margin-top: 8px; }

  .person {
    position: absolute; left: 30px; top: 211px;
  }
  .person-name {
    font-family: 'Montserrat', sans-serif; font-weight: 700;
    font-size: 22px; color: var(--brand-red); letter-spacing: 0.3px;
  }
  .person-title {
    font-family: 'Roboto', sans-serif; font-weight: 300;
    font-size: 16px; color: var(--ink-dark);
  }

  .divider { position: absolute; left: 0; top: 0; }

  .address {
    position: absolute; left: 30px; top: 300px;
    font-family: 'Roboto', sans-serif; font-weight: 300; font-style: normal;
    font-size: 16px; line-height: 24px; color: var(--ink-dark);
  }

  .contact-list {
    position: absolute; right: 30px; top: 278px;
    list-style: none;
    font-family: 'Roboto', sans-serif; font-weight: 300;
    font-size: 16px; line-height: 24px; color: var(--ink-dark);
  }
  .contact-list li {
    display: flex; align-items: center; justify-content: flex-end; gap: 10px;
  }
  .contact-list svg { width: 15px; height: 15px; flex: none; }
</style>
</head>
<body>
<main class="canvas">

  <section class="card card--front" aria-label="Card front">
    <div class="front-lockup">
      <div class="brand-square"></div>
      <div class="firm-name">DARA WHITMORE, CPA, LLC</div>
      <div class="firm-tagline">CERTIFIED PUBLIC ACCOUNTANT</div>
      <div class="firm-services">ACCOUNTING, TAX &amp; CONSULTING SERVICES</div>
    </div>
  </section>

  <section class="card card--back" aria-label="Card back">
    <div class="back-lockup">
      <div class="brand-square"></div>
      <div>
        <div class="firm-name">DARA WHITMORE, CPA, LLC</div>
        <div class="firm-tagline">CERTIFIED PUBLIC ACCOUNTANT</div>
        <div class="firm-services">ACCOUNTING, TAX &amp; CONSULTING SERVICES</div>
      </div>
    </div>

    <div class="person">
      <div class="person-name">DARA WHITMORE</div>
      <div class="person-title">Principal</div>
    </div>

    <svg class="divider" width="621" height="375" viewBox="0 0 621 375" aria-hidden="true">
      <path d="M30 276 H300 C335 276 340 252 380 252 H590" fill="none" stroke="var(--rule)" stroke-width="2"/>
    </svg>

    <address class="address">
      4821, Larkfield Avenue, Suite 210<br>
      Ashbrook, US 28801
    </address>

    <ul class="contact-list">
      <li>704-555-0186
        <svg viewBox="0 0 16 16" aria-hidden="true"><path d="M2 6c0-2 3-3 6-3s6 1 6 3v1h-3V6H5v1H2z M4 8h8l1 5H3z" fill="var(--brand-red)"/><circle cx="8" cy="10.5" r="1.4" fill="#f2f2f2"/></svg>
      </li>
      <li>dw@darawhitmorecpa.com
        <svg viewBox="0 0 16 16" aria-hidden="true"><rect x="1" y="3" width="14" height="10" fill="var(--brand-red)"/><path d="M1.5 3.5 8 9l6.5-5.5 M1.5 12.5 6 7.5 M14.5 12.5 10 7.5" fill="none" stroke="#f2f2f2" stroke-width="1.1"/></svg>
      </li>
      <li>www.darawhitmorecpa.com
        <svg viewBox="0 0 16 16" aria-hidden="true"><circle cx="8" cy="8" r="7" fill="var(--brand-red)"/><path d="M1 8h14 M8 1v14 M8 1c-3 3-3 11 0 14 M8 1c3 3 3 11 0 14 M2.5 4.5h11 M2.5 11.5h11" fill="none" stroke="#f2f2f2" stroke-width="0.8"/></svg>
      </li>
    </ul>
  </section>

</main>
</body>
</html>
```